Flyer Template

I need a flyer template for door knocking on properties. Text Boxes need to be editable, with a header and text body. Footer to be my info. Project to be stylized to match my real estate signs and logo art from past projects

```html
<!DOCTYPE html>
<html lang="en">
<head>
<meta charset="utf-8">
<title>Marlow Realty – Door Knocking Flyer</title>
<link rel="stylesheet" href="https://fonts.googleapis.com/css2?family=Montserrat:wght@600;700;800&family=Questrial&display=swap">
<style>
  :root {
    --brand-red: #e8262f;
    --brand-black: #111111;
    --paper: #ffffff;
    --ink: #1c1c1c;
    --photo-light: #ece6dc;
    --photo-mid: #c9b8a2;
    --photo-dark: #5b4a40;
  }
  * { margin: 0; padding: 0; box-sizing: border-box; }
  html, body { width: 850px; height: 1200px; overflow: hidden; background: var(--paper); }
  .flyer {
    position: relative;
    width: 850px;
    height: 1200px;
    background: var(--paper);
    font-family: "Questrial", "Century Gothic", sans-serif;
    color: var(--ink);
    overflow: hidden;
  }
  .hero-photo {
    position: absolute;
    left: 0; top: 0;
    width: 454px; height: 1086px;
    background: linear-gradient(160deg, var(--photo-light) 0%, #f3efe9 30%, var(--photo-mid) 62%, var(--photo-dark) 100%);
  }
  .corner-shapes { position: absolute; left: 0; top: 0; width: 850px; height: 520px; }
  .brand {
    position: absolute;
    left: 230px; top: 212px;
    width: 430px;
    display: flex; align-items: center; justify-content: center; gap: 14px;
    color: var(--paper);
    font-family: "Montserrat", sans-serif;
    font-weight: 700;
    font-size: 25px;
    letter-spacing: 0.3px;
  }
  .brand-mark { width: 20px; height: 20px; background: var(--paper); }
  .tagline {
    position: absolute;
    left: 483px; top: 508px;
    color: var(--brand-red);
    font-size: 35px;
    line-height: 42px;
  }
  .headline {
    position: absolute;
    left: 482px; top: 552px;
    color: var(--brand-red);
    font-family: "Montserrat", sans-serif;
    font-weight: 800;
    font-size: 52px;
    line-height: 66px;
  }
  .price-quote {
    position: absolute;
    left: 483px; top: 728px;
    width: 360px;
    font-family: "Montserrat", sans-serif;
    font-weight: 600;
    font-size: 24px;
    line-height: 34px;
    color: var(--ink);
  }
  .quote-mark {
    color: var(--brand-red);
    font-family: Georgia, serif;
    font-weight: 700;
    font-size: 58px;
    line-height: 0;
    vertical-align: -18px;
  }
  .quote-mark.open { margin-right: 2px; }
  .quote-mark.close { margin-left: 8px; }
  .body-copy {
    position: absolute;
    left: 485px; top: 819px;
    width: 330px;
    font-size: 17px;
    line-height: 21.7px;
    color: var(--ink);
  }
  .features {
    position: absolute;
    left: 132px; top: 850px;
    color: var(--brand-red);
    font-family: "Montserrat", sans-serif;
    font-weight: 700;
    font-size: 21.5px;
    line-height: 29.5px;
  }
  .features-title { font-size: 20.5px; line-height: 29.5px; font-weight: 700; }
  .features-list { list-style: none; }
  .features-list li::before { content: "•"; margin-right: 8px; }
  .footer {
    position: absolute;
    left: 0; top: 1086px;
    width: 850px; height: 114px;
    display: flex;
  }
  .footer-name {
    width: 454px;
    background: var(--brand-red);
    color: var(--paper);
    font-family: "Montserrat", sans-serif;
    font-weight: 600;
    font-size: 33px;
    letter-spacing: 0.5px;
    display: flex; align-items: center;
    padding-left: 29px;
  }
  .footer-contact {
    flex: 1;
    background: var(--brand-black);
    color: var(--paper);
    font-family: "Montserrat", sans-serif;
    font-weight: 600;
    padding: 16px 0 0 40px;
  }
  .footer-phone { font-size: 37px; line-height: 44px; letter-spacing: 0.5px; }
  .footer-email { font-size: 19.5px; line-height: 32px; }
</style>
</head>
<body>
<main class="flyer">
  <div class="hero-photo" role="img" aria-label="Photo of a smiling young family: mother and daughter playing with the father on a sofa"></div>

  <svg class="corner-shapes" viewBox="0 0 850 520" aria-hidden="true">
    <polygon points="0,0 850,0 850,57 454,447" fill="var(--brand-red)"/>
    <polygon points="850,57 850,161 454,514 454,447" fill="var(--brand-black)"/>
    <polygon points="454,447 454,514 850,161 850,1200 454,1200" fill="var(--paper)"/>
    <rect x="454" y="514" width="396" height="10" fill="var(--paper)"/>
  </svg>

  <div class="brand"><span class="brand-mark"></span><span class="brand-name">MARLOW REALTY</span></div>

  <p class="tagline">a right choice for</p>
  <h1 class="headline">YOUR BIG<br>DREAMS</h1>

  <p class="price-quote"><span class="quote-mark open">“</span>ELEGANT HOMES FOR<br>SALE $ 2,500,000<span class="quote-mark close">”</span></p>

  <p class="body-copy">Lorem Ipsum is simply dummy text of the printing and typesetting industry. Lorem Ipsum has been the industry's standard dummy text ever since the 1500s, when an unknown printer took a galley of type and scrambled it to make a type specimen book. It has survived not only five centuries, but also the leap into electronic typesetting, remaining essential.</p>

  <section class="features">
    <h2 class="features-title">AWESOME FEATURES</h2>
    <ul class="features-list">
      <li>4 Bedroom</li>
      <li>Kitchen Room</li>
      <li>Guest Room</li>
      <li>Laundry Room</li>
      <li>2 Living Room</li>
      <li>Swimming Pool</li>
    </ul>
  </section>

  <footer class="footer">
    <div class="footer-name">JORDAN MARLOW</div>
    <div class="footer-contact">
      <p class="footer-phone">907-555-0148</p>
      <p class="footer-email">JMARLOW@MAILBOX.COM</p>
    </div>
  </footer>
</main>
</body>
</html>
```